The Lindenmoor Compass Book

Cover Design for my first book. The book is for elementary school principals who are unhappy and are considering a career change but are afraid to leave. I teach them how to develop emotional fitness and resiliency through thought management so that they can decide whether to stay or leave their position from a place of empowerment. I've attached my podcast artwork for your reference. My publisher suggested not having me on the cover which is fine. I just thought it might be helpful.

Target Market(s)

Elementary School Principals

Industry/Entity Type

Education

Logo Text

The Lindenmoor Compass

Font styles to use
Serif
Sans Serif

Colors
34a6d7
33b8a4
3276b5

Requirements
Must have
• Title, Author name, photo or artwork that captures the essence of the book

```html
<!DOCTYPE html>
<html lang="en">
<head>
<meta charset="utf-8">
<title>The Lindenmoor Compass Book Cover</title>
<link rel="stylesheet" href="https://fonts.googleapis.com/css2?family=Oswald:wght@300;600&family=Josefin+Sans:wght@300;400&display=swap">
<style>
  :root {
    --page-bg: #f3f3f3;
    --cover-pink: #ead6e1;
    --cover-blush: #f1e6ee;
    --cover-white: #ffffff;
    --title-yellow: #e8e01c;
    --title-ink: #141414;
    --band-blue: #1a87c9;
    --band-text: #ffffff;
  }
  html, body {
    margin: 0;
    padding: 0;
    width: 1005px;
    height: 1200px;
    overflow: hidden;
    background: var(--page-bg);
  }
  .canvas {
    position: relative;
    width: 1005px;
    height: 1200px;
  }
  .cover {
    position: absolute;
    left: 112px;
    top: 45px;
    width: 780px;
    height: 1110px;
    overflow: hidden;
    background: var(--cover-white);
    box-shadow: 0 6px 24px rgba(0,0,0,0.12);
  }
  .cover-art {
    position: absolute;
    inset: 0 0 0 0;
    width: 100%;
    height: 100%;
  }
  .title-block {
    position: absolute;
    top: 150px;
    left: 0;
    width: 100%;
    text-align: center;
  }
  .title-kicker {
    font-family: "Josefin Sans", sans-serif;
    font-weight: 400;
    font-size: 30px;
    letter-spacing: 10px;
    color: var(--title-ink);
    margin: 0 0 8px 10px;
  }
  .title-main {
    font-family: "Oswald", sans-serif;
    font-weight: 600;
    font-size: 118px;
    line-height: 1;
    letter-spacing: 4px;
    color: var(--title-yellow);
    margin: 0;
  }
  .title-sub {
    font-family: "Josefin Sans", sans-serif;
    font-weight: 300;
    font-size: 96px;
    line-height: 1;
    letter-spacing: 22px;
    color: var(--title-ink);
    margin: 14px 0 0 22px;
  }
  .author-band {
    position: absolute;
    left: 0;
    top: 970px;
    width: 100%;
    height: 74px;
    background: var(--band-blue);
    display: flex;
    align-items: center;
    justify-content: center;
  }
  .author-name {
    font-family: "Oswald", sans-serif;
    font-weight: 300;
    font-size: 46px;
    letter-spacing: 5px;
    word-spacing: 10px;
    color: var(--band-text);
  }
</style>
</head>
<body>
<div class="canvas">
  <div class="cover">
    <svg class="cover-art" viewBox="0 0 780 1110" preserveAspectRatio="none" role="img" aria-label="Photograph of a row of glossy blue balls with sad faces and one yellow ball with a smile, on a soft pink backdrop">
      <defs>
        <linearGradient id="backdrop" x1="0" y1="0" x2="0" y2="1">
          <stop offset="0" stop-color="var(--cover-blush)"/>
          <stop offset="0.55" stop-color="var(--cover-pink)"/>
          <stop offset="0.78" stop-color="#f2f0f4"/>
          <stop offset="1" stop-color="var(--cover-white)"/>
        </linearGradient>
        <linearGradient id="ballrow" x1="0" y1="0" x2="1" y2="0">
          <stop offset="0" stop-color="#1f9fdc" stop-opacity="0.55"/>
          <stop offset="0.35" stop-color="#f4e83a" stop-opacity="0.55"/>
          <stop offset="0.6" stop-color="#1f9fdc" stop-opacity="0.5"/>
          <stop offset="1" stop-color="#1f9fdc" stop-opacity="0.3"/>
        </linearGradient>
      </defs>
      <rect width="780" height="1110" fill="url(#backdrop)"/>
      <rect x="90" y="600" width="620" height="220" rx="110" fill="url(#ballrow)"/>
    </svg>

    <div class="title-block">
      <p class="title-kicker">THE</p>
      <h1 class="title-main">LINDENMOOR</h1>
      <p class="title-sub">COMPASS</p>
    </div>

    <div class="author-band">
      <span class="author-name">MARISOL HALE BRENNAN</span>
    </div>
  </div>
</div>
</body>
</html>
```